Pro-life non-profit needs a dynamic poster design for their Christmas Gala.

We need a poster design which plays off the name of the event, The Silver Lantern. The Silver Lantern, of course is the Baby Jesus. Our cause supports unborn children in Iowa. The gala will include a concert of popular Christmas music sung by top soloists backed by an orchestra. An original commissioned song, The Silver Lantern, will be premiered. Purple and gold colors immediately come to mind, but a designer should not feel constrained on colors. We need an editable design w/fonts. Photoshop w/layers or Illustrator files are good.

```html
<!DOCTYPE html>
<html lang="en">
<head>
<meta charset="utf-8">
<title>The Silver Lantern – A Pro-Life Christmas Gala</title>
<link rel="stylesheet" href="https://fonts.googleapis.com/css2?family=Teko:wght@400;500;600&family=Saira+Condensed:wght@400;500;600&family=Great+Vibes&display=swap">
<style>
  :root {
    --stage: #b443c4;
    --purple-deep: #3a0b5e;
    --purple-mid: #6d1a9c;
    --purple-bright: #a52fc9;
    --magenta: #c93fb8;
    --gold: #f5cf3c;
    --gold-light: #fff2a8;
    --gold-dark: #c9951c;
    --white: #ffffff;
    --badge-red: #9c1420;
  }
  * { margin: 0; padding: 0; box-sizing: border-box; }
  html, body { width: 1200px; height: 800px; overflow: hidden; }
  body {
    background: var(--stage);
    display: flex; align-items: center; justify-content: center;
  }
  .flyer {
    position: relative;
    width: 570px; height: 760px;
    overflow: hidden;
    background:
      radial-gradient(ellipse at 50% 40%, rgba(233,120,230,.55) 0%, rgba(165,47,201,.35) 35%, transparent 65%),
      linear-gradient(180deg, var(--purple-mid) 0%, var(--purple-bright) 40%, var(--purple-mid) 70%, var(--purple-deep) 100%);
    box-shadow: 0 20px 50px rgba(60,0,80,.45);
    text-align: center;
    color: var(--white);
  }
  .flyer__glow {
    position: absolute; left: 0; right: 0; top: 0; height: 180px;
    background: linear-gradient(180deg, rgba(201,63,184,.6), transparent);
  }
  .flyer__floor {
    position: absolute; left: 0; right: 0; bottom: 0; height: 260px;
    background: linear-gradient(180deg, transparent, rgba(40,6,66,.85) 60%, rgba(60,10,70,.95));
  }
  .header { position: absolute; top: 34px; left: 0; right: 0; }
  .header__org {
    font-family: 'Saira Condensed', sans-serif; font-weight: 500;
    font-size: 28px; letter-spacing: 1px; line-height: 1;
  }
  .header__presents {
    font-family: 'Saira Condensed', sans-serif; font-size: 17px; line-height: 1.2;
  }
  .header__event {
    font-family: 'Saira Condensed', sans-serif; font-size: 17px;
    letter-spacing: 5px; margin-top: 4px;
  }
  .hero-image {
    position: absolute; left: 170px; top: 128px; width: 240px; height: 290px;
    border-radius: 110px 110px 20px 20px;
    background: linear-gradient(180deg, #e9b54a 0%, #e8c9a8 22%, #7da3cf 40%, #c42a2a 62%, #efe6d6 85%, rgba(109,26,156,0) 100%);
    opacity: .9;
  }
  .date-badge {
    position: absolute; left: 372px; top: 196px; width: 112px; height: 112px;
    border-radius: 50%;
    background: radial-gradient(circle, #c0202d, var(--badge-red));
    border: 5px solid var(--white);
    display: flex; flex-direction: column; align-items: center; justify-content: center;
    font-family: 'Teko', sans-serif; color: var(--gold); line-height: .85;
  }
  .date-badge__day { font-size: 46px; font-weight: 500; }
  .date-badge__day sup { font-size: 20px; vertical-align: 22px; }
  .date-badge__month { font-size: 24px; }
  .title {
    position: absolute; top: 378px; left: 0; right: 0;
    font-family: 'Teko', sans-serif; font-weight: 600;
    font-size: 86px; line-height: .78; letter-spacing: 1px;
    color: var(--gold);
    background: linear-gradient(180deg, var(--gold-light) 0%, var(--gold) 45%, var(--gold-dark) 100%);
    -webkit-background-clip: text; background-clip: text;
    -webkit-text-fill-color: transparent;
    filter: drop-shadow(0 3px 2px rgba(50,0,40,.6));
  }
  .subtitle {
    position: absolute; top: 522px; left: 0; right: 0;
    font-family: 'Great Vibes', cursive; font-size: 38px; line-height: 1;
  }
  .details { position: absolute; top: 568px; left: 0; right: 0; }
  .details__label {
    font-family: 'Saira Condensed', sans-serif; font-size: 17px; letter-spacing: 4px;
  }
  .details__speaker {
    font-family: 'Teko', sans-serif; font-weight: 500; font-size: 38px;
    line-height: .95; color: var(--gold);
  }
  .details__line {
    font-family: 'Saira Condensed', sans-serif; font-size: 15px; letter-spacing: 2.5px; line-height: 1.35;
  }
  .details__highlight {
    font-family: 'Teko', sans-serif; font-weight: 500; font-size: 28px;
    color: var(--gold); line-height: .95; letter-spacing: .5px;
  }
  .details__small { font-family: 'Saira Condensed', sans-serif; font-size: 13px; letter-spacing: 1.5px; line-height: 1.3; }
  .details__link { color: var(--gold); }
  .contact {
    position: absolute; bottom: 16px; left: 0; right: 0;
    display: flex; justify-content: center; gap: 18px; align-items: center;
    font-family: 'Saira Condensed', sans-serif; font-size: 13px; letter-spacing: 1px;
  }
  .contact__item { display: flex; align-items: center; gap: 6px; }
  .contact__icon { width: 16px; height: 16px; fill: var(--white); }
  .pin { width: 12px; height: 14px; fill: var(--white); vertical-align: -2px; }
</style>
</head>
<body>
  <article class="flyer">
    <div class="flyer__glow"></div>
    <div class="flyer__floor"></div>

    <header class="header">
      <div class="header__org">HEARTLAND HOPE ALLIANCE</div>
      <div class="header__presents">PRESENTS</div>
      <div class="header__event">THE TENTH ANNUAL FUNDRAISING BANQUET</div>
    </header>

    <div class="hero-image" role="img" aria-label="Painted statue of a crowned mother holding a sleeping child"></div>

    <div class="date-badge">
      <span class="date-badge__day">21<sup>ST</sup></span>
      <span class="date-badge__month">NOVEMBER</span>
    </div>

    <h1 class="title">THE SILVER<br>LANTERN</h1>
    <p class="subtitle">A Pro-Life Christmas Gala</p>

    <section class="details">
      <div class="details__label">SPECIAL GUEST SPEAKER</div>
      <div class="details__speaker">BISHOP DANIEL MARLOW</div>
      <div class="details__line">OPEN 05.30 PM | $60 PERSON | $500 TABLE OF TEN</div>
      <div class="details__highlight">COCKTAILS · DINNER · CHRISTMAS CONCERT</div>
      <div class="details__line">
        <svg class="pin" viewBox="0 0 12 14"><path d="M6 0a5 5 0 0 0-5 5c0 4 5 9 5 9s5-5 5-9a5 5 0 0 0-5-5zm0 7a2 2 0 1 1 0-4 2 2 0 0 1 0 4z"/></svg>
        MAPLE GROVE HALL, CEDAR FALLS, IA
      </div>
      <div class="details__small">SEATING LIMITED · RESERVATIONS NEEDED</div>
      <div class="details__small">ORDER TICKETS ONLINE: <span class="details__link">WWW.HEARTLANDHOPE.ORG</span></div>
    </section>

    <footer class="contact">
      <span class="contact__item">
        <svg class="contact__icon" viewBox="0 0 16 16"><path d="M4 0h8a1 1 0 0 1 1 1v14a1 1 0 0 1-1 1H4a1 1 0 0 1-1-1V1a1 1 0 0 1 1-1zm1 2v10h6V2zm3 11a1 1 0 1 0 0 2 1 1 0 0 0 0-2z"/></svg>
        555-014-2290
      </span>
      <span class="contact__item">
        <svg class="contact__icon" viewBox="0 0 16 16"><path d="M0 3h16v10H0zm1.5 1.2 6.5 5 6.5-5z"/></svg>
        EVENTS@HEARTLANDHOPE.ORG
      </span>
      <span class="contact__item">
        <svg class="contact__icon" viewBox="0 0 16 16"><circle cx="8" cy="8" r="7" fill="none" stroke="#fff" stroke-width="1.5"/><path d="M1 8h14M8 1c-3 3-3 11 0 14M8 1c3 3 3 11 0 14" fill="none" stroke="#fff" stroke-width="1.2"/></svg>
        WWW.HEARTLANDHOPE.ORG
      </span>
    </footer>
  </article>
</body>
</html>
```